edgy fitness flyer

Utilize quote
"I don't want a great body"
by: Nobody Ever
Offer oin back . Vard needs to be edgy and sexy.

Target Market(s)

Women and men 25-45

Industry/Entity Type

Fitness

Requirements
Must have
• clear font layered over gradient image
• See attached sample.
• bright and eye catching
• must coordniate with studio image
• www.plovarfitness.com

```html
<!DOCTYPE html>
<html lang="en">
<head>
<meta charset="utf-8">
<title>Plovar Fitness Flyer</title>
<link rel="stylesheet" href="https://fonts.googleapis.com/css2?family=Bebas+Neue&display=swap">
<style>
  :root {
    --stage: #e2e2e2;
    --charcoal: #414141;
    --orange: #f0822f;
    --orange-soft: #f6a765;
    --white: #ffffff;
    --ink: #3a3a3a;
  }
  * { box-sizing: border-box; margin: 0; padding: 0; }
  html, body { width: 1200px; height: 960px; overflow: hidden; }
  body {
    background: var(--stage);
    font-family: "Bebas Neue", "Arial Narrow", sans-serif;
    position: relative;
  }
  .page {
    position: absolute;
    top: 86px;
    width: 550px;
    height: 782px;
    overflow: hidden;
    box-shadow: 0 2px 8px rgba(0,0,0,.35);
  }
  .page--front { left: 36px; background: var(--charcoal); }
  .page--back {
    left: 610px;
    background: linear-gradient(180deg, var(--white) 0%, #fbe3cf 30%, var(--orange-soft) 65%, var(--orange) 100%);
  }

  .brand { position: absolute; line-height: 1; white-space: nowrap; }
  .brand__name { color: var(--orange); display: block; letter-spacing: .5px; }
  .brand__tagline { color: var(--charcoal); font-size: 8px; letter-spacing: .3px; display: block; margin-top: 3px; }
  .page--front .brand { left: 58px; top: 46px; }
  .page--front .brand__name { font-size: 32px; }
  .page--front .brand__tagline { color: var(--orange); }
  .page--back .brand { left: 364px; top: 42px; }
  .page--back .brand__name { font-size: 24px; }

  .quote { position: absolute; left: 128px; top: 606px; color: var(--white); }
  .quote__text { font-size: 36px; letter-spacing: .5px; line-height: 1; }
  .quote__author { font-size: 19px; margin-left: 184px; margin-top: 4px; line-height: 1; }

  .classes__title {
    position: absolute; left: 55px; top: 40px;
    font-size: 38px; color: var(--charcoal); letter-spacing: .5px; line-height: 1;
    font-weight: normal;
  }
  .class { position: absolute; left: 55px; width: 300px; }
  .class__name {
    display: block; width: 180px; height: 27px;
    background: var(--charcoal); color: var(--orange);
    font-size: 24px; line-height: 29px; padding-left: 4px;
    font-weight: normal;
  }
  .class__desc { margin-top: 8px; color: var(--ink); font-size: 16.5px; line-height: 22px; }

  .art { position: absolute; inset: 0; width: 550px; height: 782px; }

  .photo { position: absolute; }
  .photo--circle {
    width: 146px; height: 146px; border-radius: 50%;
    border: 3px solid var(--white);
  }
  .photo--breath { left: 357px; top: 113px; background: radial-gradient(circle at 35% 40%, #c98b55, #4a2b17 70%); }
  .photo--cycling { left: 357px; top: 245px; background: radial-gradient(circle at 50% 50%, #8a8580, #2a2626 75%); }
  .photo--yoga { left: 357px; top: 376px; background: radial-gradient(circle at 45% 45%, #dfe2e4, #9aa5ab 75%); }
  .photo--athlete {
    left: 290px; top: 530px; width: 260px; height: 172px;
    background: linear-gradient(90deg, rgba(120,110,100,0) 0%, #8d8580 35%, #c9c3bd 65%, #6f6a66 100%);
  }

  .cta {
    position: absolute; left: 179px; top: 641px; width: 198px; height: 61px;
    background: var(--white); color: var(--orange);
    font-size: 34px; line-height: 64px; text-align: center;
  }
  .footer {
    position: absolute; left: 0; bottom: 0; width: 550px; height: 80px;
    background: var(--charcoal); color: var(--orange);
    font-size: 28px; line-height: 84px; text-align: center; letter-spacing: .5px;
  }
</style>
</head>
<body>

  <section class="page page--front">
    <div class="brand">
      <span class="brand__name">PLOVAR FITNESS</span>
      <span class="brand__tagline">BUILDING BODIES FROM THE GROUND UP</span>
    </div>
    <blockquote class="quote">
      <p class="quote__text">"I DON'T WANT A GREAT BODY"</p>
      <p class="quote__author">BY: NOBODY EVER</p>
    </blockquote>
  </section>

  <section class="page page--back">
    <svg class="art" viewBox="0 0 550 782" aria-hidden="true">
      <path d="M550 112 C 480 330, 400 520, 265 702 L550 702 Z" fill="var(--charcoal)"/>
      <path d="M550 102 C 470 330, 385 520, 250 702" fill="none" stroke="var(--orange)" stroke-width="5"/>
    </svg>

    <div class="photo photo--athlete" role="img" aria-label="Close-up photo of an intense athlete mid-workout"></div>
    <div class="photo photo--circle photo--breath" role="img" aria-label="Photo of an athlete catching breath after training"></div>
    <div class="photo photo--circle photo--cycling" role="img" aria-label="Photo of a row of indoor cycling bikes"></div>
    <div class="photo photo--circle photo--yoga" role="img" aria-label="Photo of a woman in a yoga stretch"></div>

    <h2 class="classes__title">OUR CLASSES:</h2>
    <div class="brand">
      <span class="brand__name">PLOVAR FITNESS</span>
      <span class="brand__tagline">BUILDING BODIES FROM THE GROUND UP</span>
    </div>

    <article class="class" style="top:101px">
      <h3 class="class__name">GRIT40</h3>
      <p class="class__desc">40 MINUTES. 700 CALORIES<br>DESIGNED FOR ALL FITNESS LEVELS, GRIT40 IS<br>GUARANTEED TO BRING OUT YOUR “INNER ATHLETE”</p>
    </article>
    <article class="class" style="top:211px">
      <h3 class="class__name">RIDING HARD</h3>
      <p class="class__desc">WHETHER YOU'RE AN AVID OUTDOOR<br>CYCLIST OR A WEEKEND WARRIOR, WE<br>HAVE A CYCLING TRAINING SESSION FOR YOU.</p>
    </article>
    <article class="class" style="top:318px">
      <h3 class="class__name">GOTTA TABATA</h3>
      <p class="class__desc">WITH 6 FUNCTIONAL EXERCISES<br>IN 8 MINUTES, WORKING TO FAILURE<br>NEVER FELT SO GOOD!</p>
    </article>
    <article class="class" style="top:424px">
      <h3 class="class__name">LET IT FLOW</h3>
      <p class="class__desc">VINYASA FLOW<br>POWER FLOW<br>RESTORATIVE YOGA</p>
    </article>
    <article class="class" style="top:530px">
      <h3 class="class__name">THE AMP'D WORKOUT</h3>
      <p class="class__desc">KEEP MOVING FOR 20 MINUTES NON<br>STOP REPEATING 3 LOW REPETITION<br>EXERCISES FOR 20 MINUTES.</p>
    </article>

    <div class="cta">BOOK NOW</div>
    <footer class="footer">WWW.PLOVARFITNESS.COM</footer>
  </section>

</body>
</html>
```